Need Business Card for our Real Estate Business with Sales Executive's Picture

PANTONE 484 C ( RED)

PANTONE 2766 C ( BLUE

Industry/Entity Type

Real Estate

Contact Information for Business Card

Name, Mobile, email, & picture of Person
Agency Phone, address, Web address

Requirements
Must have
• Our Logo Colours, Agent Picture,

```html
<!DOCTYPE html>
<html lang="en">
<head>
<meta charset="UTF-8">
<title>Meridian – Business Card</title>
<link href="https://fonts.googleapis.com/css2?family=Cinzel:wght@500&family=Noto+Serif:wght@400&family=Quicksand:wght@400&display=swap" rel="stylesheet">
<style>
  :root {
    --navy: #051637;
    --paper: #e8e6e7;
    --ink: #1e1e22;
    --maroon: #7a1518;
    --white: #ffffff;
    --photo-tone: #c9cdd6;
  }
  * { margin: 0; padding: 0; box-sizing: border-box; }
  html, body { width: 1200px; height: 1200px; overflow: hidden; background: var(--white); }
  .canvas { position: relative; width: 1200px; height: 1200px; }

  .card { position: absolute; left: 175px; width: 851px; height: 473px; }
  .card-front { top: 94px; background: var(--paper); }
  .card-back { top: 634px; background: var(--navy); }

  .photo-panel { position: absolute; left: 0; top: 0; width: 283px; height: 100%; background: var(--navy); }
  .agent-photo {
    position: absolute; left: 35px; top: 96px; width: 213px; height: 280px;
    border: 6px solid var(--white);
    background: linear-gradient(90deg, #e3e5e2 0%, #2a3f86 30%, #1f3272 65%, #e6e8e4 100%);
  }

  .brand {
    position: absolute; display: flex; align-items: center; gap: 10px;
    font-family: "Cinzel", serif; font-weight: 500; font-size: 36px; letter-spacing: 2px;
  }
  .brand-mark { width: 12px; height: 12px; background: var(--maroon); }
  .brand-front { left: 316px; top: 208px; color: var(--navy); }
  .brand-back { left: 0; right: 0; justify-content: center; top: 250px; color: var(--white); }

  .divider { position: absolute; left: 553px; top: 166px; width: 3px; height: 140px; background: var(--navy); }

  .contact { position: absolute; left: 573px; top: 162px; }
  .agent-name {
    font-family: "Noto Serif", serif; font-size: 26px; color: var(--maroon);
    text-decoration: underline; text-decoration-thickness: 2px; text-underline-offset: 3px;
    margin-left: 20px; line-height: 34px;
  }
  .contact-list { list-style: none; font-family: "Quicksand", sans-serif; font-size: 19px; color: var(--ink); }
  .contact-list li { position: relative; padding-left: 22px; line-height: 23px; }
  .contact-list li.gap { margin-top: 1px; }
  .contact-list svg { position: absolute; left: 0; top: 4px; width: 16px; height: 16px; }
</style>
</head>
<body>
<div class="canvas">

  <section class="card card-front">
    <div class="photo-panel">
      <div class="agent-photo" role="img" aria-label="Portrait of the sales executive in a navy suit"></div>
    </div>

    <div class="brand brand-front"><span class="brand-mark"></span>MERIDIAN</div>

    <div class="divider"></div>

    <div class="contact">
      <p class="agent-name">Arjun Malhotra</p>
      <ul class="contact-list">
        <li>
          <svg viewBox="0 0 16 16"><circle cx="8" cy="8" r="8" fill="var(--ink)"/><path d="M5 4 L7 4 L7.6 6 L6.6 7 Q7.5 9 9 9.6 L10 8.6 L12 9.2 L12 11 Q8 12 5 8 Q4 6 5 4Z" fill="var(--white)"/></svg>
          Mobile Phone
        </li>
        <li>Agency Phone</li>
        <li class="gap">
          <svg viewBox="0 0 16 16"><circle cx="8" cy="8" r="7.2" fill="none" stroke="var(--ink)" stroke-width="1.6"/><rect x="4" y="5.2" width="8" height="5.6" fill="none" stroke="var(--ink)" stroke-width="1.1"/><path d="M4 5.2 L8 8.6 L12 5.2" fill="none" stroke="var(--ink)" stroke-width="1.1"/></svg>
          Email
        </li>
        <li class="gap">
          <svg viewBox="0 0 16 16"><circle cx="8" cy="8" r="8" fill="var(--ink)"/><path d="M8 13 L5.4 8 A3 3 0 1 1 10.6 8 Z" fill="var(--white)"/><circle cx="8" cy="6.4" r="1.1" fill="var(--ink)"/></svg>
          Adress
        </li>
        <li>Wedsite</li>
      </ul>
    </div>
  </section>

  <section class="card card-back">
    <div class="brand brand-back"><span class="brand-mark"></span>MERIDIAN</div>
  </section>

</div>
</body>
</html>
```